New Business Card Design for Manufacturing

We are an engineering/manufacturing company that offers Advanced machining/assembly/engineering services, as well as innovative products for the heavy duty engine cooling markets.

We are looking to get a new business card designed that is clean and modern looking, but still fits the wide range of technical/skilled work we do.

- We hope to use this design as the base for other design work in new Presentations, web, and print work.

Industry/Entity Type

Engineering

Contact Information for Business Card

Our preferred color of blue is (RGB) 22/71/159 but can vary slightly from that color. Our content will be our Logo and full company name (Corvath Tooling Works, Inc.), company address, name, job title, phone number with extension, cell number, fax number, website, and email address on the cards.
We'd like the full company name next to the logo, but we are open to other interpretations of that layout.
Preferably, we would like the back side to be clean with just our logo, and the front to contain all of the contact information.

Colors
2f74b4
0355a3
85abd2

Requirements
Must have
• - Logo, company name, needed content - We are open to interpretation beyond that.
• - Standard size business card.
• - Horizontal orientation.
• - Enough space for lengthy names / job titles (for example, a job title could read "Directory of Human Resources" or "V.P. of Governmental Affairs"). We need this to look clean, whether the title be short (CEO) or long (as described above).

```html
<!DOCTYPE html>
<html lang="en">
<head>
<meta charset="utf-8">
<title>Corvath Tooling Works – Business Card</title>
<link rel="stylesheet" href="https://fonts.googleapis.com/css2?family=Roboto:wght@400;700;900&family=Roboto+Condensed:wght@700&display=swap">
<style>
  :root {
    --backdrop: #2a2a2a;
    --card-white: #f3f3f3;
    --brand-blue: #0f52a0;
    --ink: #111111;
    --ink-soft: #555555;
    --rule: #9a9a9a;
    --white: #ffffff;
  }
  * { margin: 0; padding: 0; box-sizing: border-box; }
  html, body { width: 1200px; height: 960px; overflow: hidden; }
  body {
    background: var(--backdrop);
    position: relative;
    font-family: "Roboto", Arial, sans-serif;
  }
  .card {
    position: absolute;
    width: 600px;
    height: 343px;
  }
  .card-front { left: 314px; top: 113px; background: var(--card-white); }
  .card-back  { left: 311px; top: 472px; background: var(--brand-blue); }

  /* front */
  .front-wordmark {
    position: absolute;
    right: 44px;
    top: 54px;
    display: flex;
    align-items: center;
    gap: 10px;
    color: var(--brand-blue);
    font-weight: 900;
    font-size: 40px;
    letter-spacing: 1px;
  }
  .wordmark-square {
    width: 20px; height: 20px;
    background: var(--brand-blue);
  }
  .person-name {
    position: absolute;
    left: 45px; top: 178px;
    font-family: "Roboto Condensed", Arial, sans-serif;
    font-weight: 700;
    font-size: 23px;
    color: var(--brand-blue);
  }
  .person-title {
    position: absolute;
    left: 45px; top: 204px;
    font-size: 14px;
    color: var(--ink);
  }
  .contact-list {
    position: absolute;
    left: 45px; top: 229px;
    list-style: none;
    font-size: 14px;
    color: var(--ink-soft);
  }
  .contact-list li {
    display: flex;
    align-items: center;
    height: 19px;
    white-space: nowrap;
  }
  .contact-list svg {
    width: 13px; height: 13px;
    margin-right: 9px;
    fill: var(--brand-blue);
  }
  .contact-divider {
    position: absolute;
    left: 216px; top: 270px;
    width: 1px; height: 30px;
    background: var(--rule);
  }
  .address {
    position: absolute;
    left: 240px; top: 269px;
    font-size: 14px;
    line-height: 19px;
    color: var(--ink-soft);
    font-style: normal;
    white-space: nowrap;
  }

  /* back */
  .back-lockup {
    position: absolute;
    left: 107px; top: 128px;
    display: flex;
    align-items: center;
    gap: 14px;
    color: var(--white);
    font-weight: 900;
  }
  .back-square {
    width: 26px; height: 26px;
    background: var(--white);
  }
  .back-name { font-size: 52px; letter-spacing: 1px; }
  .back-fullname {
    font-size: 17px;
    line-height: 19px;
    margin-left: 6px;
  }
</style>
</head>
<body>

<section class="card card-front" aria-label="Business card front">
  <div class="front-wordmark"><span class="wordmark-square"></span>CORVATH</div>

  <h1 class="person-name">MARTIN HALE</h1>
  <p class="person-title">V.P. of Governmental Affairs</p>

  <ul class="contact-list">
    <li>
      <svg viewBox="0 0 16 16" aria-hidden="true"><path d="M3.6 1.2l2.3 2.9c.3.4.3.9 0 1.2L4.7 6.6c.8 1.9 2.8 3.9 4.7 4.7l1.3-1.2c.3-.3.8-.3 1.2 0l2.9 2.3c.4.3.4.9.1 1.2l-1.4 1.5C9.6 16.4-.4 6.4 0.4 2.5L2 1.1c.4-.4 1.2-.3 1.6.1z"/></svg>
      614 203 5817
    </li>
    <li>
      <svg viewBox="0 0 16 16" aria-hidden="true"><path d="M4.5 0h7c.8 0 1.5.7 1.5 1.5v13c0 .8-.7 1.5-1.5 1.5h-7C3.7 16 3 15.3 3 14.5v-13C3 .7 3.7 0 4.5 0zm.5 2v10.5h6V2H5zm3 11.2a.9.9 0 100 1.8.9.9 0 000-1.8z"/></svg>
      614 770 2946
    </li>
    <li>
      <svg viewBox="0 0 16 16" aria-hidden="true"><path d="M1 3h14v1.2L8 9 1 4.2V3zm0 2.7l7 4.8 7-4.8V13H1V5.7z"/></svg>
      martin@corvath.com
    </li>
    <li>
      <svg viewBox="0 0 16 16" aria-hidden="true"><path d="M8 0a8 8 0 100 16A8 8 0 008 0zm-1 2.2c-.6.8-1.8 1.3-1.5 2.6.3 1 1.7.7 2.2 1.7.4.9-.6 1.6-.2 2.6.4 1.1 1.8.9 1.9 2.3.1 1-.5 1.9-.6 2.5A6 6 0 017 2.2zm3.5.6A6 6 0 0114 8c-.7-.4-1.5-.3-2-.9-.6-.8.1-1.9-.6-2.7-.5-.6-1.3-.5-1.5-1.1 0-.2.3-.4.6-.5z"/></svg>
      www.corvath.com
    </li>
  </ul>

  <span class="contact-divider" aria-hidden="true"></span>
  <address class="address">4120 Kestrel Way<br>Juneau, Alaska 99801</address>
</section>

<section class="card card-back" aria-label="Business card back">
  <div class="back-lockup">
    <span class="back-square"></span>
    <span class="back-name">CORVATH</span>
    <span class="back-fullname">CORVATH<br>TOOLING<br>WORKS INC</span>
  </div>
</section>

</body>
</html>
```